Website Q48 coffee

I am opening a small business selling locally roasted coffee online. To start with I want a site with three pages. 1. A welcome page with logo and mission/vision. 2. Shopping/ordering page. 3. About Us page. The brand is "Q48 Coffee - Brewed with bright hearts". We are giving back to the downs syndrome community by employing people with down syndrome (Trisomy 21) and buy donating to down syndrome research.

Target Market(s)

Families and friends of people with downs syndrome

Coding

Coded - Design and coding required

Number of Pages Required

3 page

```html
<!DOCTYPE html>
<html lang="en">
<head>
<meta charset="utf-8">
<title>Q48 Coffee - Brewed with bright hearts</title>
<link rel="stylesheet" href="https://fonts.googleapis.com/css2?family=Red+Hat+Display:wght@300;400;500;700&family=Sen:wght@400;700&display=swap">
<style>
:root{
  --ink:#111111;
  --black:#000000;
  --white:#ffffff;
  --text:#333333;
  --muted:#6b6b6b;
  --gold:#f2b705;
  --silver-1:#f4f4f4;
  --silver-2:#9a9a9a;
  --roast-1:#2a1a10;
  --roast-2:#5a3a22;
  --bean:#4a2c18;
  --mist:#ececec;
}
*{box-sizing:border-box;margin:0;padding:0}
html,body{width:1200px;height:3319px;overflow:hidden;background:var(--white)}
body{font-family:"Sen",sans-serif;color:var(--text)}
.page{position:relative;width:1200px;height:3319px;overflow:hidden}
.abs{position:absolute}
.heading{font-family:"Red Hat Display",sans-serif;font-weight:300;color:var(--ink)}
.btn{position:absolute;display:flex;align-items:center;justify-content:center;font-family:"Red Hat Display",sans-serif;font-size:16px;border-radius:8px;text-transform:uppercase;letter-spacing:.2px}
.btn-dark{background:var(--black);color:var(--white)}
.btn-ghost{border:1.5px solid var(--white);color:var(--white)}
.brand-box{position:absolute;width:89px;height:89px;border:2px solid #bdbdbd;display:flex;flex-direction:column;align-items:center;justify-content:center;color:#d8d8d8;font-family:"Red Hat Display",sans-serif;font-weight:300}
.brand-box .name{font-size:34px;line-height:1}
.brand-box .sub{font-size:12px;letter-spacing:1.5px;margin-top:2px}
.brand-box .tag{font-size:4.5px;letter-spacing:.4px;margin-top:2px}
/* hero */
.nav{position:absolute;top:24px;left:782px;display:flex;align-items:center;font-family:"Red Hat Display",sans-serif;font-size:13px;color:var(--white)}
.nav .active{border:1.5px solid var(--white);border-radius:6px;padding:7px 13px;margin-right:18px}
.nav span{margin-right:22px}
.nav .icon{width:33px;height:33px;border-radius:50%;background:var(--white);display:flex;align-items:center;justify-content:center;margin-right:8px}
.hero-title{left:58px;top:238px;font-family:"Red Hat Display",sans-serif;font-weight:500;font-size:140px;color:var(--white);letter-spacing:-4px;line-height:1}
.hero-sub{left:58px;top:396px;font-family:"Red Hat Display",sans-serif;font-weight:300;font-size:48px;line-height:52px;color:var(--white)}
.hero-tag{left:62px;top:508px;font-family:"Red Hat Display",sans-serif;font-size:21px;color:var(--white)}
/* welcome */
.photo{position:absolute}
.welcome-kicker{left:598px;top:814px;font-size:14px;color:var(--muted)}
.welcome-title{left:597px;top:834px;font-size:41px}
.block-title{font-family:"Red Hat Display",sans-serif;font-size:24px;color:var(--ink)}
.block-text{font-size:12px;line-height:19.5px;color:var(--muted);width:420px}
/* shop */
.shop-title{left:0;width:1200px;text-align:center;top:1362px;font-size:42px}
.card{position:absolute;top:1431px;width:270px;height:412px;background:var(--white);text-align:center}
.bag{position:absolute;left:83px;top:29px;width:110px;height:183px;border-radius:8px 8px 4px 4px;background:linear-gradient(160deg,#b48a62,#7a5436)}
.stars{position:absolute;top:232px;width:100%;color:var(--gold);font-size:17px;letter-spacing:2px}
.card-title{position:absolute;top:260px;width:100%;font-family:"Red Hat Display",sans-serif;font-weight:300;font-size:20px;color:var(--ink)}
.card-desc{position:absolute;top:290px;width:100%;font-size:12px;color:#444}
.card-price{position:absolute;top:314px;width:100%;font-family:"Red Hat Display",sans-serif;font-size:20px;color:var(--ink)}
.card .btn{left:68px;top:354px;width:135px;height:37px}
.view-all{left:0;width:1200px;text-align:center;top:1870px;font-family:"Red Hat Display",sans-serif;font-size:16px;text-decoration:underline;color:var(--ink)}
/* about */
.about-title{left:152px;top:2080px;font-size:33px}
.about-text{left:152px;top:2132px;width:380px;font-size:12px;line-height:19.5px;color:var(--muted)}
.about-quote{left:150px;top:2246px;width:400px;font-family:"Red Hat Display",sans-serif;font-weight:300;font-size:23px;line-height:34px;color:var(--ink)}
/* giving */
.give-text{left:655px;top:2516px;width:470px;font-family:"Sen",sans-serif;font-weight:700;font-size:20px;line-height:28.6px;color:var(--ink)}
.news-title{left:644px;top:2880px;font-family:"Red Hat Display",sans-serif;font-weight:300;font-size:23px;color:var(--white)}
.news-input{left:642px;top:2922px;width:345px;height:40px;background:var(--white);border-radius:8px;font-size:11px;color:#666;padding:14px 16px}
.news-btn{left:994px;top:2922px;width:126px;height:40px;border:1.5px solid var(--white);color:var(--white);border-radius:8px;font-size:15px}
/* footer */
.foot-desc{left:60px;top:3176px;width:260px;font-size:12px;line-height:19.5px;color:var(--white)}
.foot-head{font-family:"Red Hat Display",sans-serif;font-size:14px;color:var(--white);letter-spacing:.3px}
.foot-list{list-style:none;font-size:12px;color:var(--white)}
.foot-list li{position:relative;padding-left:18px;height:23px}
.foot-list li::before{content:"";position:absolute;left:0;top:4px;width:5px;height:5px;border:1px solid var(--white)}
.contact-row{display:flex;align-items:center;font-size:12px;color:var(--white)}
.contact-row svg{margin-right:14px}
.social{position:absolute;top:3179px;width:38px;height:38px;border:1.5px solid var(--white);border-radius:50%}
.rule{left:60px;top:3274px;width:1080px;height:1px;background:#333}
.copy{left:0;width:1200px;text-align:center;top:3290px;font-size:11px;color:var(--white)}
</style>
</head>
<body>
<div class="page">

  <!-- HERO -->
  <svg class="abs" style="left:0;top:0" width="1200" height="740" viewBox="0 0 1200 740" role="img" aria-label="Coffee beans tumbling in a roaster drum">
    <defs>
      <radialGradient id="roastGlow" cx="45%" cy="40%" r="75%">
        <stop offset="0" stop-color="#6a4529"/>
        <stop offset=".55" stop-color="#3a2416"/>
        <stop offset="1" stop-color="#120b06"/>
      </radialGradient>
    </defs>
    <path d="M0 0H1200V732C1110 660 1010 612 890 612C720 612 520 690 320 706C170 716 60 714 0 712Z" fill="url(#roastGlow)"/>
  </svg>

  <div class="brand-box" style="left:60px;top:9px">
    <div class="name">Q48</div><div class="sub">COFFEE</div><div class="tag">BREWED WITH BRIGHT HEARTS</div>
  </div>

  <nav class="nav">
    <span class="active">Home</span>
    <span>Shopping/Ordering</span>
    <span>About Us</span>
    <div class="icon" aria-label="Account">
      <svg width="16" height="16" viewBox="0 0 16 16"><circle cx="8" cy="5" r="3.3" fill="#000"/><path d="M1.5 15.5C1.5 11 4.5 9.5 8 9.5S14.5 11 14.5 15.5Z" fill="#000"/></svg>
    </div>
    <div class="icon" aria-label="Cart">
      <svg width="18" height="16" viewBox="0 0 18 16"><path d="M1 1.5H4L6 11H15L17 4H5" fill="none" stroke="#000" stroke-width="1.6" stroke-linejoin="round"/><circle cx="7" cy="14" r="1.4" fill="#000"/><circle cx="14" cy="14" r="1.4" fill="#000"/></svg>
    </div>
  </nav>

  <div class="abs hero-title">Q48</div>
  <div class="abs hero-sub">ROASTED COFFEE<br>NOW ONLINE</div>
  <div class="abs hero-tag">Brewed With Bright Hearts</div>
  <div class="btn btn-ghost" style="left:60px;top:552px;width:134px;height:40px">Shop Now</div>

  <svg class="abs" style="left:623px;top:264px" width="460" height="448" viewBox="0 0 100 96" preserveAspectRatio="none" role="img" aria-label="Cupped hands holding roasted coffee beans, in a silver heart frame">
    <defs>
      <linearGradient id="silver" x1="0" y1="0" x2="1" y2="1">
        <stop offset="0" stop-color="#ffffff"/><stop offset=".5" stop-color="#a8a8a8"/><stop offset="1" stop-color="#e6e6e6"/>
      </linearGradient>
      <radialGradient id="handsTone" cx="50%" cy="45%" r="60%">
        <stop offset="0" stop-color="#3b2417"/><stop offset=".45" stop-color="#b98a6e"/><stop offset="1" stop-color="#3a4a5e"/>
      </radialGradient>
    </defs>
    <path d="M50 22C50 22 40 2 22 4C6 6 0 22 2 36C5 58 30 76 50 96C70 76 95 58 98 36C100 22 94 6 78 4C60 2 50 22 50 22Z" fill="url(#silver)"/>
    <path transform="translate(5 5) scale(.9)" d="M50 22C50 22 40 2 22 4C6 6 0 22 2 36C5 58 30 76 50 96C70 76 95 58 98 36C100 22 94 6 78 4C60 2 50 22 50 22Z" fill="url(#handsTone)"/>
  </svg>

  <!-- WELCOME -->
  <div class="photo" style="left:60px;top:788px;width:187px;height:326px;background:linear-gradient(170deg,#5d6b78,#a8703c 55%,#6a4020)" role="img" aria-label="Roasted beans pouring from a roasting machine"></div>
  <div class="photo" style="left:264px;top:813px;width:239px;height:348px;background:linear-gradient(160deg,#2b2b2b,#6a5a50 50%,#d8cfc4)" role="img" aria-label="Two smiling café staff members in aprons"></div>

  <div class="abs welcome-kicker">Welcome To</div>
  <div class="abs heading welcome-title">Q48 COFFEE</div>
  <div class="abs block-title" style="left:602px;top:916px">Vission</div>
  <p class="abs block-text" style="left:602px;top:953px">Develop a company that markets coffee and related products to family and friends of the down syndrome community.</p>
  <div class="abs block-title" style="left:602px;top:1020px">Mission</div>
  <p class="abs block-text" style="left:602px;top:1057px">create and grow an online company selling contract roasted coffee. as growth permits become a fully vertically integrated coffee company from roasting to our own coffee shop. The company will give significant funds to medical research in downs syndrome and we will hire as many people with Downs syndrome as possible.</p>
  <div class="abs" style="left:1164px;top:1027px;width:36px;height:146px;background:linear-gradient(180deg,#f2f2f2,#8c8c8c)"></div>

  <!-- SHOP -->
  <svg class="abs" style="left:0;top:1210px" width="1200" height="810" viewBox="0 0 1200 810">
    <defs>
      <linearGradient id="mist" x1="0" y1="0" x2="0" y2="1">
        <stop offset="0" stop-color="#f6f6f6"/><stop offset=".5" stop-color="#e6e6e6"/><stop offset="1" stop-color="#efefef"/>
      </linearGradient>
    </defs>
    <path d="M0 2C150 60 300 80 520 78C760 76 960 20 1200 40V800C1080 780 980 770 860 760C600 740 300 760 0 752Z" fill="url(#mist)"/>
  </svg>
  <div class="abs" style="left:0;top:1560px;width:193px;height:386px;background:radial-gradient(ellipse at 30% 50%,#4a3a30 0%,#8a7a70 40%,rgba(230,230,230,0) 75%)" role="img" aria-label="Scattered coffee beans"></div>
  <div class="abs" style="left:1018px;top:1540px;width:182px;height:410px;background:radial-gradient(ellipse at 70% 50%,#4a3a30 0%,#8a7a70 40%,rgba(230,230,230,0) 75%)" role="img" aria-label="Scattered coffee beans"></div>

  <div class="abs heading shop-title">SHOP NOW</div>

  <div class="card" style="left:157px">
    <div class="bag" role="img" aria-label="Kraft coffee pouch"></div>
    <div class="stars">★★★★★</div>
    <div class="card-title">Q48 COFFEE</div>
    <div class="card-desc">Lorem Ipsum been the industry</div>
    <div class="card-price">$35.00</div>
    <div class="btn btn-dark">Shop Now</div>
  </div>
  <div class="card" style="left:465px">
    <div class="bag" role="img" aria-label="Kraft coffee pouch"></div>
    <div class="stars">★★★★★</div>
    <div class="card-title">Q48 COFFEE</div>
    <div class="card-desc">Lorem Ipsum been the industry</div>
    <div class="card-price">$35.00</div>
    <div class="btn btn-dark">Shop Now</div>
  </div>
  <div class="card" style="left:772px">
    <div class="bag" role="img" aria-label="Kraft coffee pouch"></div>
    <div class="stars">★★★★★</div>
    <div class="card-title">Q48 COFFEE</div>
    <div class="card-desc">Lorem Ipsum been the industry</div>
    <div class="card-price">$35.00</div>
    <div class="btn btn-dark">Shop Now</div>
  </div>

  <div class="abs view-all">View All Products</div>

  <!-- ABOUT -->
  <div class="abs heading about-title">About Us</div>
  <p class="abs about-text">Lorem Ipsum has been the industry's standard dummy text ever since the 1500s, when an unknown printer took a galley of type and scrambled it to make a type specimen book. It has survived not only five centuries, but also the leap into electronic typesetting, remaining essentially unchanged.</p>
  <div class="abs about-quote">Coffee Is Our Passion, Our Fun, And Part Of Our Identity. Join Our Family. Join The Fun.</div>
  <div class="btn btn-dark" style="left:152px;top:2361px;width:142px;height:40px">Learn More</div>
  <div class="abs" style="left:528px;top:2050px;width:583px;height:354px;background:radial-gradient(ellipse at 72% 70%,#f3ede4 0%,#c9b8a4 22%,#5a3520 45%,rgba(255,255,255,0) 70%)" role="img" aria-label="Coffee cup with heart-shaped steam beside spilled beans"></div>

  <!-- GIVING BACK -->
  <svg class="abs" style="left:0;top:2690px" width="1200" height="629" viewBox="0 0 1200 629">
    <path d="M0 4C200 70 420 150 600 140C800 128 920 30 1200 10V629H0Z" fill="#000"/>
  </svg>

  <svg class="abs" style="left:119px;top:2520px" width="461" height="451" viewBox="0 0 100 96" preserveAspectRatio="none" role="img" aria-label="Team member scooping coffee beans into a jar, in a silver heart frame">
    <defs>
      <radialGradient id="scoopTone" cx="50%" cy="50%" r="60%">
        <stop offset="0" stop-color="#8a7060"/><stop offset=".5" stop-color="#5a4a40"/><stop offset="1" stop-color="#2e2a28"/>
      </radialGradient>
    </defs>
    <path d="M50 22C50 22 40 2 22 4C6 6 0 22 2 36C5 58 30 76 50 96C70 76 95 58 98 36C100 22 94 6 78 4C60 2 50 22 50 22Z" fill="url(#silver)"/>
    <path transform="translate(5 5) scale(.9)" d="M50 22C50 22 40 2 22 4C6 6 0 22 2 36C5 58 30 76 50 96C70 76 95 58 98 36C100 22 94 6 78 4C60 2 50 22 50 22Z" fill="url(#scoopTone)"/>
  </svg>

  <p class="abs give-text">We are Giving back to the downs Syndrome Community by Employing People With Down Syndrome (Trisomy 21) and Buy Donating to Down Syndrome Research.</p>
  <div class="btn btn-dark" style="left:656px;top:2650px;width:134px;height:40px">Shop Now</div>

  <div class="abs news-title">Newsletter Signup !</div>
  <div class="abs news-input">Enter Email *</div>
  <div class="btn news-btn">Subscribe</div>

  <!-- FOOTER -->
  <div class="brand-box" style="left:60px;top:3070px">
    <div class="name">Q48</div><div class="sub">COFFEE</div><div class="tag">BREWED WITH BRIGHT HEARTS</div>
  </div>
  <p class="abs foot-desc">Develop a company that markets coffee and related products to family and friends of the down syndrome community.</p>

  <div class="abs foot-head" style="left:337px;top:3068px">SITEMAP</div>
  <ul class="abs foot-list" style="left:336px;top:3107px">
    <li>Home</li><li>Shopping/Ordering</li><li>About Us</li>
  </ul>

  <div class="abs foot-head" style="left:612px;top:3068px">CONTACT US</div>
  <div class="abs contact-row" style="left:611px;top:3104px">
    <svg width="20" height="20" viewBox="0 0 20 20"><path d="M4 2L7 2L8.5 6L6.5 7.5C7.5 10 10 12.5 12.5 13.5L14 11.5L18 13V16C18 17 17 18 16 18C8.5 17.5 2.5 11.5 2 4C2 3 3 2 4 2Z" fill="none" stroke="#fff" stroke-width="1.5" stroke-linejoin="round"/></svg>
    +1 555 014 2048
  </div>
  <div class="abs contact-row" style="left:611px;top:3140px">
    <svg width="20" height="16" viewBox="0 0 20 16"><rect x="1" y="1" width="18" height="14" rx="1.5" fill="#fff"/><path d="M1.5 2L10 9L18.5 2" fill="none" stroke="#000" stroke-width="1.4"/></svg>
    info@q48coffee.com
  </div>
  <div class="social" style="left:611px" aria-label="Social profile"></div>
  <div class="social" style="left:653px" aria-label="Social profile"></div>
  <div class="social" style="left:696px" aria-label="Social profile"></div>

  <div class="abs foot-head" style="left:887px;top:3068px">USEFULL LINKS</div>
  <ul class="abs foot-list" style="left:886px;top:3107px">
    <li>Donations</li><li>Help</li><li>Privacy Policy</li><li>Terms &amp; Conditions</li>
  </ul>

  <div class="abs rule"></div>
  <div class="abs copy">©Q48COFFEE - 2021 All rights reserved.</div>
</div>
</body>
</html>
```